Magazine Ad for the Waste Industry

We need a full page ad design that will help us introduce our new engine cooling system into the Waste market. This system helps regulate engine temperatures for large trash trucks with its advanced technology and durable. We would like this ad to make an impact and stand out from the more cluttered looking ads that are seen in trade magazines.
The project must be submitted in either InDesign or Photoshop files.

Target Market(s)

Waste Industry, Trash truck manufacturers

Industry/Entity Type

Waste Management

Font styles to use
Sans Serif

Colors
0255a3

Requirements
Must have
• The text and images attached with a more modern industrial/masculine feel.
• Our Company colors are...
• Blue (RGB 25, 76, 159)
• Gray (RGB 129, 130, 133)
• White and black as accents as needed
• SIZING
• Spread Bleed: 9.5" x 11.375"
Nice to have
• I attached two files for a font that we have used in the past. Another font we use commonly is Ariel.

```html
<!DOCTYPE html>
<html lang="en">
<head>
<meta charset="utf-8">
<title>Norvale CoreFlow – Advanced Electric Engine Cooling</title>
<link rel="stylesheet" href="https://fonts.googleapis.com/css2?family=Oswald:wght@300;400&family=Source+Sans+3:wght@400;600;700&display=swap">
<style>
  :root {
    --brand-blue: #194c9f;
    --accent-blue: #0255a3;
    --deep-navy: #050a2a;
    --mid-navy: #0c1a6e;
    --vivid-blue: #1a2fb8;
    --brand-gray: #818285;
    --white: #ffffff;
    --backdrop: #eceef1;
  }
  * { box-sizing: border-box; margin: 0; padding: 0; }
  html, body { width: 1200px; height: 1200px; overflow: hidden; }
  body {
    background: var(--backdrop);
    font-family: "Source Sans 3", Arial, sans-serif;
    position: relative;
  }
  .ad-page {
    position: absolute;
    left: 200px; top: 80px;
    width: 800px; height: 1040px;
    overflow: hidden;
    background: linear-gradient(180deg, var(--deep-navy) 0%, var(--mid-navy) 38%, var(--vivid-blue) 72%, var(--mid-navy) 100%);
    color: var(--white);
    box-shadow: 0 10px 30px rgba(0,0,0,.25);
  }
  .product-mark {
    position: absolute; top: 58px; left: 0; width: 100%;
    display: flex; flex-direction: column; align-items: center; gap: 10px;
  }
  .product-mark__dot {
    width: 64px; height: 64px; border-radius: 50%; background: var(--white);
  }
  .product-mark__name {
    font-weight: 700; font-size: 28px; letter-spacing: 1px; text-transform: uppercase;
  }
  .headline {
    position: absolute; top: 190px; left: 0; width: 100%;
    text-align: center;
    font-family: "Oswald", Arial, sans-serif; font-weight: 300;
    font-size: 66px; line-height: 1.08; letter-spacing: 1px;
  }
  .product-visual {
    position: absolute; left: 0; top: 370px; width: 310px; height: 400px;
    background: linear-gradient(135deg, #3a3d45 0%, #1b1d22 60%, #5c6070 100%);
    border-radius: 0 6px 6px 0;
  }
  .feature-panel {
    position: absolute; left: 340px; top: 370px; width: 420px; height: 270px;
    background: rgba(20, 40, 160, 0.55);
    padding: 34px 30px;
    display: flex; flex-direction: column; justify-content: space-between;
  }
  .feature {
    display: flex; align-items: center; gap: 12px;
    font-size: 20px; font-weight: 600;
  }
  .feature svg { flex: none; }
  .company-blurb {
    position: absolute; left: 60px; top: 800px; width: 690px;
    font-size: 14px; line-height: 1.35;
  }
  .contact-band {
    position: absolute; left: 0; bottom: 0; width: 100%; height: 130px;
    background: var(--white);
    display: flex; align-items: center;
  }
  .contact-band__brand {
    width: 250px; height: 100%;
    display: flex; align-items: center; justify-content: center;
    border-right: 2px solid #d6d7d9;
    font-weight: 700; font-size: 40px; color: var(--brand-blue);
  }
  .contact-band__details {
    flex: 1; display: flex; justify-content: space-around; align-items: center;
    font-size: 22px; color: #222;
  }
  .contact-band__details span { display: flex; align-items: center; gap: 6px; }
</style>
</head>
<body>
  <article class="ad-page">
    <div class="product-mark">
      <div class="product-mark__dot"></div>
      <div class="product-mark__name">CoreFlow</div>
    </div>

    <h1 class="headline">ADVANCED ELECTRIC<br>ENGINE COOLING</h1>

    <div class="product-visual" role="img" aria-label="Electric engine cooling unit with four reversible fans in a black housing"></div>

    <ul class="feature-panel">
      <li class="feature"><svg width="18" height="18" viewBox="0 0 18 18"><circle cx="9" cy="9" r="9" fill="#fff"/><path d="M5 9.5l2.6 2.5L13 6.5" stroke="#0c1a6e" stroke-width="2.2" fill="none"/></svg>Fully reversible fans</li>
      <li class="feature"><svg width="18" height="18" viewBox="0 0 18 18"><circle cx="9" cy="9" r="9" fill="#fff"/><path d="M5 9.5l2.6 2.5L13 6.5" stroke="#0c1a6e" stroke-width="2.2" fill="none"/></svg>Eliminate preventative maintenance</li>
      <li class="feature"><svg width="18" height="18" viewBox="0 0 18 18"><circle cx="9" cy="9" r="9" fill="#fff"/><path d="M5 9.5l2.6 2.5L13 6.5" stroke="#0c1a6e" stroke-width="2.2" fill="none"/></svg>Average 8% fuel economy</li>
      <li class="feature"><svg width="18" height="18" viewBox="0 0 18 18"><circle cx="9" cy="9" r="9" fill="#fff"/><path d="M5 9.5l2.6 2.5L13 6.5" stroke="#0c1a6e" stroke-width="2.2" fill="none"/></svg>Increase Horsepower</li>
      <li class="feature"><svg width="18" height="18" viewBox="0 0 18 18"><circle cx="9" cy="9" r="9" fill="#fff"/><path d="M5 9.5l2.6 2.5L13 6.5" stroke="#0c1a6e" stroke-width="2.2" fill="none"/></svg>Quieter Residential Operation</li>
    </ul>

    <p class="company-blurb">Norvale is a diversified manufacturer. Our products are found in a wide range of global industries. Norvale was built on its expertise in complex, precision machining, low and high volume assembly, and engineering capabilities that includes developing electric components and systems for a wide array of markets. Norvale's products and services can be found in the following list of key industries below. Mouse over each image for a detailed explanation of how Norvale has been involved with that industry.</p>

    <footer class="contact-band">
      <div class="contact-band__brand">Norvale</div>
      <div class="contact-band__details">
        <span><svg width="14" height="14" viewBox="0 0 14 14"><circle cx="7" cy="7" r="6" fill="none" stroke="#222" stroke-width="1.5"/><path d="M1 7h12M7 1c-3 3.5-3 8.5 0 12M7 1c3 3.5 3 8.5 0 12" fill="none" stroke="#222" stroke-width="1"/></svg>www.norvale-corp.com/refuse</span>
        <span><svg width="16" height="16" viewBox="0 0 24 24"><path d="M6.6 10.8a15 15 0 006.6 6.6l2.2-2.2c.3-.3.7-.4 1-.2 1.1.4 2.3.6 3.6.6.6 0 1 .4 1 1V20c0 .6-.4 1-1 1A17 17 0 013 4c0-.6.4-1 1-1h3.5c.6 0 1 .4 1 1 0 1.3.2 2.5.6 3.6.1.3 0 .7-.2 1z" fill="#222"/></svg>(555) 014-2297</span>
      </div>
    </footer>
  </article>
</body>
</html>
```